PowerPoint template for large technology company

Requesting proposals for a PowerPoint deck template that can be used by our sales team when pitching clients. We are a large technology media company, that is BtoB focused, and are looking for a professional, clean, tech-forward, design and layout. However, our clients are advertisers and brands who would respond well to a subtly stylized creative design.

We need a fully built-out template wherein our sales team can choose from a variety of slide layouts while compiling their pitch decks.

Key objective: To create a template that mandates consistent fonts, sizes, and layout, and is easy to use for novice presenters. A plug-and-play template.

Secondary objective: A refresh on current design of company template.

Presentation template should include:
2 Presentation title slide options
2 Section header options
6 information layout slide options
3 data charts (pie, bar, and column)
Summary/ Thank you slide

The teams using this template will not be adept with PowerPoint but should easily be able to insert images and text boxes without it ruining the design and format of the presentation. The idea is if 20 people use our template to build pitch-decks, all of the individual decks should all look like they came from the same team. Please be as detailed and specific as possible when building out slides.

Simple, high-compatibility fonts. Please see brand guidelines attached.

Target Market(s)

Large advertising agencies and major consumer technology brands.

This deck template will not be consumer facing.

Industry/Entity Type

Building

Font styles to use
Serif
Sans Serif

Requirements
Must have
• Must be clean, high-tech, and forces user to stay within template guidelines during modifications.

Template should be built out for a sales presentation that will be a tool for ppt novices.
Nice to have
• As we are revamping existing decks, it will be nice to see multiple ideas on the design. Think professional, high-tech, and powerful.
Should not have
• Should not have a distracting background that will interfere with presentations or where it will be difficult to easily insert images.

Blacked out backgrounds cause a "boxed in" look for images and/or text boxes - which is undesirable. Either don't include color-blocked backgrounds or introduce a way in which this can be used that avoids the previously stated pitfall.

No rotated text-fill options. (i.e. rotating text by 90 or 180 degrees)

Please don't be too literal in your design approach.

```html
<!DOCTYPE html>
<html lang="en">
<head>
<meta charset="utf-8">
<title>Project Title Slide</title>
<link rel="stylesheet" href="https://fonts.googleapis.com/css2?family=Questrial&family=Arimo:wght@400&family=Open+Sans:wght@400&display=swap">
<style>
  :root {
    --blue-deep: #0a3f9e;
    --blue-mid: #2f7fd6;
    --blue-light: #9fd0f2;
    --blue-glow: #e2f3fd;
    --band-white: #ffffff;
    --ink-dark: #2e3a44;
    --ink-title: #3c4148;
    --ink-accent: #7f96a8;
    --ink-body: #3a3a3a;
  }
  * { margin: 0; padding: 0; box-sizing: border-box; }
  html, body { width: 1200px; height: 900px; overflow: hidden; }
  body { position: relative; background: var(--blue-deep); }

  .slide { position: relative; width: 1200px; height: 900px; overflow: hidden; }

  .hero-image {
    position: absolute; inset: 0;
    background:
      radial-gradient(ellipse 260px 200px at 490px 230px, var(--blue-glow) 0%, rgba(226,243,253,0.6) 45%, rgba(226,243,253,0) 100%),
      radial-gradient(ellipse 120px 100px at 880px 310px, rgba(2,10,40,0.85) 0%, rgba(2,10,40,0) 100%),
      radial-gradient(ellipse 90px 120px at 0px 200px, rgba(2,10,40,0.7) 0%, rgba(2,10,40,0) 100%),
      radial-gradient(ellipse 600px 360px at 560px 300px, var(--blue-light) 0%, rgba(159,208,242,0) 100%),
      linear-gradient(180deg, var(--blue-mid) 0%, var(--blue-deep) 60%, var(--blue-mid) 100%);
  }

  .title-band {
    position: absolute; left: 0; top: 555px;
    width: 1200px; height: 180px;
    background: var(--band-white);
  }

  .brand {
    position: absolute; left: 105px; top: 0;
    height: 180px;
    display: flex; align-items: center;
  }
  .brand-name {
    font-family: "Open Sans", sans-serif;
    font-weight: 400;
    font-size: 64px;
    line-height: 1;
    letter-spacing: -1px;
    color: var(--ink-dark);
  }

  .project {
    position: absolute; left: 568px; top: 26px;
  }
  .project-title {
    font-family: "Questrial", sans-serif;
    font-weight: 400;
    font-size: 50px;
    line-height: 1.1;
    color: var(--ink-title);
  }
  .project-title .accent { color: var(--ink-accent); }
  .project-summary {
    font-family: "Arimo", sans-serif;
    font-size: 21.5px;
    line-height: 32px;
    color: var(--ink-body);
    margin-top: 10px;
    width: 400px;
  }
</style>
</head>
<body>
  <main class="slide">
    <div class="hero-image" role="img" aria-label="Blurred close-up photograph of a glowing blue circuit board"></div>

    <section class="title-band">
      <div class="brand">
        <div class="brand-name">Brightnode</div>
      </div>

      <div class="project">
        <h1 class="project-title">Project <span class="accent">Title here</span></h1>
        <p class="project-summary">Lorem ipsum dolor sit Lorem ipsum dolor sit Lorem ipsum dolor sit Lorem ipsum</p>
      </div>
    </section>
  </main>
</body>
</html>
```